Save our Business Card - We need your help

We need a fresh look on our business cards. We like it as it is, but it's not quite getting the 'wow' effect that we desire.
We're a tech startup building a cloud based solution for retailers consisting of Point of Sale, Inventory management and CRM.
The design should communicate a sense of a company that cares about the little things, design and relationships.
You can have a look at our website www.brimvale.com to get a feel for what we're like. Please feel free to message us for any further clarification
Our Customers are retail busines owners, cafe owners, other startups etc.
Building

```html
<!DOCTYPE html>
<html lang="en">
<head>
<meta charset="utf-8">
<title>Brimvale Business Card</title>
<link href="https://fonts.googleapis.com/css2?family=Lato:wght@400;700&display=swap" rel="stylesheet">
<style>
  :root {
    --backdrop: #4b4b4d;
    --card-dark: #3e3e40;
    --card-light: #ffffff;
    --brand-orange: #f7931e;
    --ink: #3d3d3f;
    --ink-soft: #444446;
  }
  * { margin: 0; padding: 0; box-sizing: border-box; }
  html, body {
    width: 1200px; height: 1000px; overflow: hidden;
    background: var(--backdrop);
    font-family: "Lato", sans-serif;
  }
  .canvas { position: relative; width: 1200px; height: 1000px; }

  .card { position: absolute; box-shadow: 0 10px 22px rgba(0,0,0,.45); }

  .card-back {
    left: 172px; top: 126px; width: 594px; height: 366px;
    background: var(--card-dark);
    display: flex; align-items: center; justify-content: center; gap: 16px;
  }
  .card-back .brand-mark { width: 56px; height: 56px; background: var(--brand-orange); }
  .card-back .brand-name { font-size: 44px; font-weight: 700; color: var(--brand-orange); }

  .card-front {
    left: 450px; top: 541px; width: 590px; height: 364px;
    background: var(--card-light); overflow: hidden;
  }
  .brand {
    position: absolute; left: 42px; top: 56px;
    display: flex; align-items: center; gap: 18px;
  }
  .brand-mark { width: 64px; height: 64px; background: var(--brand-orange); }
  .brand-name { font-size: 46px; font-weight: 700; color: var(--brand-orange); letter-spacing: -0.5px; }

  .person { position: absolute; left: 42px; top: 165px; }
  .person-name { font-size: 20px; font-weight: 700; color: var(--brand-orange); line-height: 24px; }
  .person-role { font-size: 15px; color: var(--ink); line-height: 20px; }

  .contacts, .address {
    position: absolute; top: 227px; list-style: none;
    font-size: 13.5px; color: var(--ink-soft); line-height: 22.5px;
  }
  .contacts { left: 42px; }
  .contacts li { display: flex; align-items: center; gap: 7px; }
  .contacts svg { width: 16px; height: 16px; flex: none; }
  .address { left: 366px; }

  .footer-band { position: absolute; left: 0; bottom: 0; width: 590px; height: 36px; }
</style>
</head>
<body>
<main class="canvas">

  <section class="card card-back" aria-label="Business card back">
    <span class="brand-mark"></span>
    <span class="brand-name">Brimvale</span>
  </section>

  <section class="card card-front" aria-label="Business card front">
    <div class="brand">
      <span class="brand-mark"></span>
      <span class="brand-name">Brimvale</span>
    </div>

    <div class="person">
      <p class="person-name">Daniel Harlow</p>
      <p class="person-role">President</p>
    </div>

    <ul class="contacts">
      <li>
        <svg viewBox="0 0 16 16" aria-hidden="true"><path d="M4 1.5 6.5 4.5 5 6.2c.8 1.8 2.2 3.3 4 4.2l1.6-1.5 3 2.4-1.6 2.7C7.5 14 2 8.5 2 3.2Z" fill="none" stroke="var(--brand-orange)" stroke-width="1.6" stroke-linejoin="round"/></svg>
        <span>123 456 7890</span>
      </li>
      <li>
        <svg viewBox="0 0 16 16" aria-hidden="true"><rect x="4.5" y="1" width="7" height="14" rx="1.2" fill="none" stroke="var(--brand-orange)" stroke-width="1.6"/><circle cx="8" cy="12.6" r=".9" fill="var(--brand-orange)"/></svg>
        <span>123 456 7890</span>
      </li>
      <li>
        <svg viewBox="0 0 16 16" aria-hidden="true"><rect x="1" y="3.5" width="14" height="9.5" fill="var(--brand-orange)"/><path d="M1 3.5 8 9l7-5.5" fill="none" stroke="#fff" stroke-width="1.2"/></svg>
        <span>support@brimvale.com</span>
      </li>
      <li>
        <svg viewBox="0 0 16 16" aria-hidden="true"><circle cx="8" cy="8" r="6.8" fill="var(--brand-orange)"/><path d="M4 4.5c1.5.3 2 1.5 3.3 1.5.8 1.2-.6 2-1.5 2.6-.5 1 .4 2.7-.5 3.5M10 2.8c-.5 1.2.5 2 1.6 1.7M9.5 9c1.2-.4 2.6.2 3 1.3" fill="none" stroke="#fff" stroke-width="1.1"/></svg>
        <span>www.brimvale.com</span>
      </li>
    </ul>

    <ul class="address">
      <li>Unit D-4-12, Block D</li>
      <li>22 Jalan Meranti Utama</li>
      <li>PJU3B, 47410 Kota Damai</li>
      <li>Selangor, Malaysia</li>
    </ul>

    <svg class="footer-band" viewBox="0 0 590 36" aria-hidden="true">
      <polygon points="0,14 342,14 338,36 0,36" fill="var(--card-dark)"/>
      <path d="M342,36 L350,12 Q354,0 368,0 L590,0 L590,36 Z" fill="var(--brand-orange)"/>
    </svg>
  </section>

</main>
</body>
</html>
```